Need a FLYER/BROCHURE for selling woman hair. I have an online business and need your help.

I need a flyer/BROCHURE that represents my company. We sale hair online and needing for our customers to know our prices and discounts for any holiday and upcoming new year specials. I need the brochure to stand out. Have our brand Logo on it. Pictures of hair we sale on our site and models on the flyer. Prices will need to be place on the flyer indicating before and after the discounts. I also have a bag gift for loyal customers that need to be on the flyer. Colors I am interested in are purple and Gold. Or something creative that will blend with my logo. On my prices I sent. I need to change the title Best, Medium and Low Quality to 6A, 5A, to The Orlena Selection.

Reason: I would like the deadline to change. The reason I see some designers are coming to my project and some are saying the deadline is too short. I would like to see what they can offer me before I decide.

Industry/Entity Type

Business

Requirements
Must have
• Pictures of my brand. Prices that matches my original prices and sales prices. Pictures of hair and models.

```html
<!DOCTYPE html>
<html lang="en">
<head>
<meta charset="utf-8">
<title>The Orlena Selection – Flyer and Price List</title>
<link rel="stylesheet" href="https://fonts.googleapis.com/css2?family=Open+Sans:wght@300;400;600;700&display=swap">
<style>
  :root{
    --purple-deep:#3d2378;
    --purple:#5b2d8e;
    --purple-bright:#7a3aa6;
    --gold:#c6a05a;
    --gold-light:#e3c98a;
    --gold-dark:#a98440;
    --cream:#f3ead9;
    --white:#ffffff;
    --stage:#e6e4e1;
  }
  *{box-sizing:border-box;margin:0;padding:0}
  html,body{width:1200px;height:786px;overflow:hidden;background:var(--stage);font-family:"Open Sans",Arial,sans-serif;color:var(--white)}
  .canvas{position:relative;width:1200px;height:786px}
  .sheet{position:absolute;top:75px;width:612px;height:792px;transform:scale(0.8186);transform-origin:0 0;background:var(--gold);overflow:hidden;box-shadow:0 4px 14px rgba(0,0,0,.25)}
  .sheet--flyer{left:75px}
  .sheet--prices{left:627px}
  .abs{position:absolute}
  .photo{position:absolute}
  .photo--hero{left:0;top:0;width:612px;height:410px;background:linear-gradient(100deg,#1b1410 0%,#3a2a20 40%,#8a6248 68%,#c8b3a3 100%)}
  .swoosh,.footer-band,.header-band{position:absolute;left:0;width:612px}
  .brand{position:absolute;font-weight:600;text-transform:uppercase;letter-spacing:2px;display:flex;align-items:center;gap:10px}
  .brand__dot{width:14px;height:14px;border-radius:50%;background:currentColor;flex:none}
  .brand--flyer{left:50px;top:120px;color:var(--gold-light);font-size:20px}
  .tagline{left:38px;top:198px;font-size:19px;font-weight:300;color:var(--cream)}
  .promise{left:23px;top:316px;font-size:18.5px;line-height:26px}
  .gift{left:408px;top:302px;width:192px;height:192px;border-radius:50%;background:var(--gold);padding:8px}
  .gift__inner{width:100%;height:100%;border-radius:50%;background:var(--cream);display:flex;flex-direction:column;align-items:center;padding-top:14px}
  .photo--bag{position:static;width:86px;height:102px;border-radius:6px;background:linear-gradient(180deg,#5a5a5a,#a7a7a7 55%,#3a3a3a)}
  .gift__title{margin-top:6px;font-size:13px;font-weight:700;color:#2f2a26}
  .gift__sub{font-size:9.5px;font-weight:600;color:#2f2a26}
  .section-title{left:29px;top:476px;font-size:17.5px}
  .mission{left:29px;top:513px;width:296px;font-size:12.2px;line-height:16.8px;text-align:justify}
  .offer{left:380px;top:524px;width:220px;text-align:center;font-size:24px;line-height:33px;font-weight:400}
  .promo{left:378px;top:602px;width:224px;text-align:center;font-size:10.5px}
  .specials{left:24px;top:694px;width:104px;height:72px;border-radius:50%;background:radial-gradient(circle at 40% 35%,var(--gold-light),var(--gold-dark));border:2px solid var(--cream);color:var(--purple-deep);font-size:9.6px;font-weight:600;line-height:12px;text-align:center;display:flex;align-items:center;justify-content:center;text-transform:uppercase}
  .contact{left:176px;top:698px;width:270px;text-align:center}
  .contact__call{font-size:23px;color:var(--gold-light);font-weight:400}
  .contact__mail{font-size:11.5px;margin-top:4px}
  .contact__web{font-size:17px;letter-spacing:1.3px;margin-top:2px}

  .header-top{left:0;top:0;width:612px;height:170px;background:var(--cream)}
  .photo--model-left{left:0;top:0;width:215px;height:165px;background:linear-gradient(110deg,#2a1d17,#6e4a36 55%,#b08e78)}
  .photo--model-right{left:398px;top:0;width:214px;height:165px;background:linear-gradient(250deg,#2a1d17,#6a4632 55%,#b59582)}
  .brand--prices{left:222px;top:80px;width:168px;justify-content:center;color:var(--purple);font-size:14px;letter-spacing:1px}
  .price-title{left:0;top:142px;width:612px;text-align:center;font-size:30px;font-weight:400;letter-spacing:1px}
  .price-group{position:absolute;width:118px}
  .price-group__title{font-size:9.8px;font-weight:600;text-transform:uppercase;margin-bottom:5px;white-space:nowrap}
  .price-group__note{font-size:6.5px;font-weight:600;text-transform:uppercase;margin:-5px 0 4px}
  .price-row{display:flex;font-size:8.6px;line-height:13.7px}
  .price-row__len{white-space:nowrap}
  .price-row__dots{flex:1;border-bottom:1px dotted var(--white);margin:0 1px 4px}
  .photo--bundles{left:420px;top:612px;width:190px;height:180px;background:radial-gradient(ellipse at 60% 50%,#151515 0%,#2e2e2e 45%,rgba(46,46,46,0) 72%)}
</style>
</head>
<body>
<main class="canvas">

  <!-- Front flyer -->
  <section class="sheet sheet--flyer">
    <div class="photo photo--hero" role="img" aria-label="Model with long dark natural hair, hands framing her face"></div>

    <div class="brand brand--flyer"><span class="brand__dot"></span>The Orlena Selection</div>
    <p class="abs tagline">Beautiful. Colorful. You.</p>

    <svg class="swoosh" style="top:260px" width="612" height="180" viewBox="0 260 612 180" aria-hidden="true">
      <defs>
        <linearGradient id="swooshFill" x1="0" x2="1">
          <stop offset="0" stop-color="#6a2c91"/><stop offset="1" stop-color="#4b2a8a"/>
        </linearGradient>
      </defs>
      <path d="M0 298 C150 270 310 296 430 378 C300 402 130 400 0 420 Z" fill="url(#swooshFill)"/>
      <path d="M0 292 C160 262 330 290 460 382" fill="none" stroke="#e3c98a" stroke-width="5"/>
      <path d="M0 420 C130 400 300 402 430 378 L612 410 L612 440 L0 440 Z" fill="#c6a05a"/>
    </svg>
    <p class="abs promise">Hair you can depend to last<br>and share the beauty in you!</p>

    <div class="abs gift">
      <div class="gift__inner">
        <div class="photo photo--bag" role="img" aria-label="Drawstring gift bag"></div>
        <div class="gift__title">BAG GIFT</div>
        <div class="gift__sub">FOR LOYAL CUSTOMERS</div>
      </div>
    </div>

    <h2 class="abs section-title" style="font-weight:400">100% NATURAL HUMAN HAIR</h2>
    <p class="abs mission">Our mission is to give the best experience in selling the top quality natural human hair. Our hair are from different regions across the world. They are well prepared and managed to keep you looking good for a long period of time. We welcome you to our brand to be part of our family.</p>

    <p class="abs offer">New Customer<br>gets 10% off</p>
    <p class="abs promo">PROMO CODE: ORLENANEWCUSTOMER</p>

    <svg class="footer-band" style="top:640px" width="612" height="152" viewBox="0 640 612 152" aria-hidden="true">
      <defs>
        <linearGradient id="footFillA" x1="0" x2="1">
          <stop offset="0" stop-color="#6a2c91"/><stop offset=".5" stop-color="#4b2a8a"/><stop offset="1" stop-color="#6a2c91"/>
        </linearGradient>
      </defs>
      <path d="M0 672 C150 650 250 660 306 676 C362 660 462 650 612 670 L612 792 L0 792 Z" fill="url(#footFillA)"/>
      <path d="M0 668 C150 646 250 656 306 672 C362 656 462 646 612 666" fill="none" stroke="#e3c98a" stroke-width="3"/>
    </svg>
    <div class="abs specials">Holiday and<br>upcoming<br>new year<br>specials</div>
    <div class="abs contact">
      <div class="contact__call">Call Now:&nbsp; 901-555-0174</div>
      <div class="contact__mail">customerservice@orlenaselection.com</div>
      <div class="contact__web">www.orlenaselection.com</div>
    </div>
  </section>

  <!-- Price list -->
  <section class="sheet sheet--prices">
    <div class="abs header-top"></div>
    <div class="photo photo--model-left" role="img" aria-label="Model with long wavy hair"></div>
    <div class="photo photo--model-right" role="img" aria-label="Model with long curly hair"></div>
    <div class="brand brand--prices"><span>The Orlena Selection</span></div>

    <svg class="header-band" style="top:130px" width="612" height="60" viewBox="0 130 612 60" aria-hidden="true">
      <path d="M0 152 C200 132 412 132 612 152 L612 186 L0 186 Z" fill="#4b2a8a"/>
      <line x1="0" y1="187" x2="612" y2="187" stroke="#e3c98a" stroke-width="3"/>
    </svg>
    <h1 class="abs price-title">PRICE LIST</h1>

    <div class="price-group" style="left:23px;top:210px">
      <h3 class="price-group__title">High Quality</h3>
      <div class="price-row"><span class="price-row__len">12 inch</span><span class="price-row__dots"></span><span>$55</span></div>
      <div class="price-row"><span class="price-row__len">14 inch</span><span class="price-row__dots"></span><span>$62</span></div>
      <div class="price-row"><span class="price-row__len">16 inch</span><span class="price-row__dots"></span><span>$74</span></div>
      <div class="price-row"><span class="price-row__len">18 inch</span><span class="price-row__dots"></span><span>$81</span></div>
      <div class="price-row"><span class="price-row__len">20 inch</span><span class="price-row__dots"></span><span>$88</span></div>
      <div class="price-row"><span class="price-row__len">22 inch</span><span class="price-row__dots"></span><span>$97</span></div>
      <div class="price-row"><span class="price-row__len">24 inch</span><span class="price-row__dots"></span><span>$107</span></div>
      <div class="price-row"><span class="price-row__len">26 inch</span><span class="price-row__dots"></span><span>$112</span></div>
      <div class="price-row"><span class="price-row__len">28 inch</span><span class="price-row__dots"></span><span>$120</span></div>
      <div class="price-row"><span class="price-row__len">30 inch</span><span class="price-row__dots"></span><span>$128</span></div>
    </div>

    <div class="price-group" style="left:173px;top:212px">
      <h3 class="price-group__title">Medium Quality</h3>
      <div class="price-row"><span class="price-row__len">12 inch</span><span class="price-row__dots"></span><span>$43</span></div>
      <div class="price-row"><span class="price-row__len">14 inch</span><span class="price-row__dots"></span><span>$48</span></div>
      <div class="price-row"><span class="price-row__len">16 inch</span><span class="price-row__dots"></span><span>$53</span></div>
      <div class="price-row"><span class="price-row__len">18 inch</span><span class="price-row__dots"></span><span>$59</span></div>
      <div class="price-row"><span class="price-row__len">20 inch</span><span class="price-row__dots"></span><span>$64</span></div>
      <div class="price-row"><span class="price-row__len">22 inch</span><span class="price-row__dots"></span><span>$69</span></div>
      <div class="price-row"><span class="price-row__len">24 inch</span><span class="price-row__dots"></span><span>$80</span></div>
      <div class="price-row"><span class="price-row__len">26 inch</span><span class="price-row__dots"></span><span>$85</span></div>
      <div class="price-row"><span class="price-row__len">28 inch</span><span class="price-row__dots"></span><span>$91</span></div>
      <div class="price-row"><span class="price-row__len">30 inch</span><span class="price-row__dots"></span><span>$96</span></div>
      <div class="price-row"><span class="price-row__len">32 inch</span><span class="price-row__dots"></span><span>$98</span></div>
      <div class="price-row"><span class="price-row__len">34 inch</span><span class="price-row__dots"></span><span>$99</span></div>
      <div class="price-row"><span class="price-row__len">36 inch</span><span class="price-row__dots"></span><span>$104</span></div>
      <div class="price-row"><span class="price-row__len">38 inch</span><span class="price-row__dots"></span><span>$107</span></div>
      <div class="price-row"><span class="price-row__len">40 inch</span><span class="price-row__dots"></span><span>$114</span></div>
    </div>

    <div class="price-group" style="left:327px;top:210px">
      <h3 class="price-group__title">Bast Lace Closure</h3>
      <div class="price-row"><span class="price-row__len">12 inch</span><span class="price-row__dots"></span><span>$64</span></div>
      <div class="price-row"><span class="price-row__len">14 inch</span><span class="price-row__dots"></span><span>$70</span></div>
      <div class="price-row"><span class="price-row__len">16 inch</span><span class="price-row__dots"></span><span>$78</span></div>
      <div class="price-row"><span class="price-row__len">18 inch</span><span class="price-row__dots"></span><span>$86</span></div>
      <div class="price-row"><span class="price-row__len">20 inch</span><span class="price-row__dots"></span><span>$92</span></div>
      <div class="price-row"><span class="price-row__len">22 inch</span><span class="price-row__dots"></span><span>$102</span></div>
      <div class="price-row"><span class="price-row__len">24 inch</span><span class="price-row__dots"></span><span>$104</span></div>
    </div>

    <div class="price-group" style="left:477px;top:210px">
      <h3 class="price-group__title">Cheap Lace Closure</h3>
      <div class="price-row"><span class="price-row__len">12 inch</span><span class="price-row__dots"></span><span>$43</span></div>
      <div class="price-row"><span class="price-row__len">14 inch</span><span class="price-row__dots"></span><span>$48</span></div>
      <div class="price-row"><span class="price-row__len">16 inch</span><span class="price-row__dots"></span><span>$53</span></div>
      <div class="price-row"><span class="price-row__len">18 inch</span><span class="price-row__dots"></span><span>$58</span></div>
      <div class="price-row"><span class="price-row__len">20 inch</span><span class="price-row__dots"></span><span>$62</span></div>
      <div class="price-row"><span class="price-row__len">22 inch</span><span class="price-row__dots"></span><span>$66</span></div>
    </div>

    <div class="price-group" style="left:327px;top:362px">
      <h3 class="price-group__title">Bast Lace Frontal <small style="font-size:6px">13*4</small></h3>
      <div class="price-row"><span class="price-row__len">12 inch</span><span class="price-row__dots"></span><span>$172</span></div>
      <div class="price-row"><span class="price-row__len">14 inch</span><span class="price-row__dots"></span><span>$177</span></div>
      <div class="price-row"><span class="price-row__len">16 inch</span><span class="price-row__dots"></span><span>$186</span></div>
      <div class="price-row"><span class="price-row__len">18 inch</span><span class="price-row__dots"></span><span>$203</span></div>
    </div>

    <div class="price-group" style="left:477px;top:362px">
      <h3 class="price-group__title">Cheap Lace Frontal <small style="font-size:6px">13*4</small></h3>
      <div class="price-row"><span class="price-row__len">12 inch</span><span class="price-row__dots"></span><span>$120</span></div>
      <div class="price-row"><span class="price-row__len">14 inch</span><span class="price-row__dots"></span><span>$126</span></div>
      <div class="price-row"><span class="price-row__len">16 inch</span><span class="price-row__dots"></span><span>$134</span></div>
      <div class="price-row"><span class="price-row__len">18 inch</span><span class="price-row__dots"></span><span>$142</span></div>
    </div>

    <div class="price-group" style="left:23px;top:473px">
      <h3 class="price-group__title">Low Quality</h3>
      <div class="price-row"><span class="price-row__len">12 inch</span><span class="price-row__dots"></span><span>$29</span></div>
      <div class="price-row"><span class="price-row__len">14 inch</span><span class="price-row__dots"></span><span>$33</span></div>
      <div class="price-row"><span class="price-row__len">16 inch</span><span class="price-row__dots"></span><span>$39</span></div>
      <div class="price-row"><span class="price-row__len">18 inch</span><span class="price-row__dots"></span><span>$42</span></div>
      <div class="price-row"><span class="price-row__len">20 inch</span><span class="price-row__dots"></span><span>$46</span></div>
      <div class="price-row"><span class="price-row__len">22 inch</span><span class="price-row__dots"></span><span>$50</span></div>
      <div class="price-row"><span class="price-row__len">24 inch</span><span class="price-row__dots"></span><span>$54</span></div>
      <div class="price-row"><span class="price-row__len">26 inch</span><span class="price-row__dots"></span><span>$59</span></div>
      <div class="price-row"><span class="price-row__len">28 inch</span><span class="price-row__dots"></span><span>$65</span></div>
      <div class="price-row"><span class="price-row__len">30 inch</span><span class="price-row__dots"></span><span>$81</span></div>
    </div>

    <div class="price-group" style="left:173px;top:473px">
      <h3 class="price-group__title">Ombre Hair</h3>
      <p class="price-group__note">Straight and body wave</p>
      <div class="price-row"><span class="price-row__len">12 inch</span><span class="price-row__dots"></span><span>$50</span></div>
      <div class="price-row"><span class="price-row__len">14 inch</span><span class="price-row__dots"></span><span>$56</span></div>
      <div class="price-row"><span class="price-row__len">16 inch</span><span class="price-row__dots"></span><span>$67</span></div>
      <div class="price-row"><span class="price-row__len">18 inch</span><span class="price-row__dots"></span><span>$74</span></div>
      <div class="price-row"><span class="price-row__len">20 inch</span><span class="price-row__dots"></span><span>$80</span></div>
      <div class="price-row"><span class="price-row__len">22 inch</span><span class="price-row__dots"></span><span>$88</span></div>
      <div class="price-row"><span class="price-row__len">24 inch</span><span class="price-row__dots"></span><span>$98</span></div>
    </div>

    <div class="price-group" style="left:327px;top:475px">
      <h3 class="price-group__title">Solid Color Hair</h3>
      <p class="price-group__note">Straight and body wave</p>
      <div class="price-row"><span class="price-row__len">18 inch</span><span class="price-row__dots"></span><span>$63</span></div>
      <div class="price-row"><span class="price-row__len">20 inch</span><span class="price-row__dots"></span><span>$72</span></div>
      <div class="price-row"><span class="price-row__len">22 inch</span><span class="price-row__dots"></span><span>$83</span></div>
      <div class="price-row"><span class="price-row__len">24 inch</span><span class="price-row__dots"></span><span>$90</span></div>
    </div>

    <div class="price-group" style="left:477px;top:475px">
      <h3 class="price-group__title">Deep Wave</h3>
      <div class="price-row" style="margin-top:7px"><span class="price-row__len">18 inch</span><span class="price-row__dots"></span><span>$66</span></div>
      <div class="price-row"><span class="price-row__len">20 inch</span><span class="price-row__dots"></span><span>$75</span></div>
      <div class="price-row"><span class="price-row__len">22 inch</span><span class="price-row__dots"></span><span>$86</span></div>
      <div class="price-row"><span class="price-row__len">24 inch</span><span class="price-row__dots"></span><span>$94</span></div>
    </div>

    <svg class="footer-band" style="top:640px" width="612" height="152" viewBox="0 640 612 152" aria-hidden="true">
      <defs>
        <linearGradient id="footFillB" x1="0" x2="1">
          <stop offset="0" stop-color="#6a2c91"/><stop offset=".5" stop-color="#4b2a8a"/><stop offset="1" stop-color="#6a2c91"/>
        </linearGradient>
      </defs>
      <path d="M0 672 C150 650 250 660 306 676 C362 660 462 650 612 670 L612 792 L0 792 Z" fill="url(#footFillB)"/>
      <path d="M0 668 C150 646 250 656 306 672 C362 656 462 646 612 666" fill="none" stroke="#e3c98a" stroke-width="3"/>
    </svg>
    <div class="photo photo--bundles" role="img" aria-label="Bundles of straight black human hair"></div>
    <div class="abs specials">Holiday and<br>upcoming<br>new year<br>specials</div>
    <div class="abs contact">
      <div class="contact__call">Call Now:&nbsp; 901-555-0174</div>
      <div class="contact__mail">customerservice@orlenaselection.com</div>
      <div class="contact__web">www.orlenaselection.com</div>
    </div>
  </section>

</main>
</body>
</html>
```